Restaurant website built on Plinko’s responsive platform- No coding skills needed

We are looking to add to our company's website www.plinkoweb.example a new inspiration page that will include examples of sites built using Plinko's platform.
In order to make it relevant, we would like to have multiple choices for every category, one of the categories is “restaurants.”

REQUIREMENTS:
o Build a "fake" restaurant site on Plinko’s responsive platform, no real restaurant information is needed. The site will include:
1. Homepage
• Restaurant header (no logo)
• Paragraph about the restaurant (can be Lorem ipsum)
• Contact details and contact buttons
• Gribbo reviews
• Reserve-a-table widget
• Open hours
2. Menu page
• You can use any menu you'd like
• Reserve a table widget
• Photo gallery
3. Footer
• Social Media links
• Map with location of restaurant

* Order of the elements is up to the designer
* Designer may add more elements as they see fit
* Designer may alter elements from page to page
* Designer will define the site color pallet and text style

****Learn more on how to create a website on Plinko's platform here
https://clipvault.example/584736201

INSTRUCTIONS FOR THIS PROJECT:
Register for a 30-day free trial for Pro access to the platform:
http://www.plinkoweb.example/plinkopro?_dm_referral=ArtHvn

a. After registering, access the dashboard and click on “Create Responsive Website.”
b. Choose a template
c. Start editing! .
d. No need to publish. When ready, take a screenshot of the preview and submit the screenshot to this ArtHaven project. Include the URL/Link to the preview within the submission description.
e. For more information on Plinko, visit the support page at https://support.plinkoweb.example/02PlinkoOne/Quick_Guide OR call our Support line Mon.-Fri., 9AM-9PM ET.1-866-555-0147

DESIGN PREFERENCES
freestyle (not related to the Plinko brand)

DESIGN SAMPLES (for inspiration)
http://www.plinkoweb.example/responsive-website/templates

What not to include in the design -
no restrictions

DELIVERABLES:
* Website on Plinko (No PSD. No coding needed)
* Screenshot preview to ArtHaven with URL/link to your site’s preview.

ABOUT THE COMPANY:
Plinko is a website builder based in California that allow designers, web designers and practically anyone to build its own site. No development and/or technical skills required.

NOTE:
* Plinko is an external site and is not part of ArtHaven
* Please refer to Plinko's Terms and Conditions for information regarding how submissions will be handled (http://www.plinkoweb.example/legal/terms)

Target Market(s)

SMBs and web designers that want to create simple, professional and beautiful websites

Industry/Entity Type

Restaurant

Number of Pages Required

2 page

Requirements
Must have
• Please send a preview of the site you created on Plinko, NOT a PSD/JPEG
Should not have
• No coding skills are needed- any web designer can build a site on Plinko

```html
<!DOCTYPE html>
<html lang="en">
<head>
<meta charset="utf-8">
<title>Restaurant Home</title>
<link rel="stylesheet" href="https://fonts.googleapis.com/css2?family=Amatic+SC:wght@400;700&family=Dancing+Script:wght@700&family=Raleway:wght@400;500;600&display=swap">
<style>
  :root {
    --bar: #1b1b1b;
    --panel: #1f1f1f;
    --ink: #ffffff;
    --muted: #cfcfcf;
    --accent: #f0531c;
    --rule: rgba(255,255,255,0.55);
    --wood-dark: #3a2618;
    --wood-mid: #6b4528;
    --wood-warm: #8c5a33;
  }
  * { margin: 0; padding: 0; box-sizing: border-box; }
  html, body { width: 1200px; height: 900px; overflow: hidden; background: var(--panel); }
  body { font-family: "Raleway", sans-serif; color: var(--ink); }

  .site-header {
    height: 64px; background: var(--bar);
    display: flex; align-items: center; justify-content: space-between;
    padding: 0 190px 0 112px; font-size: 15px; color: var(--muted);
  }
  .main-nav { display: flex; gap: 30px; font-size: 14px; }
  .main-nav a { color: var(--muted); text-decoration: none; }

  .hero {
    position: relative; height: 560px;
    display: flex; flex-direction: column; align-items: center;
  }
  .hero-photo {
    position: absolute; inset: 0;
    background:
      radial-gradient(ellipse at 70% 20%, rgba(240,235,228,0.35), transparent 35%),
      radial-gradient(ellipse at 25% 80%, rgba(210,120,50,0.45), transparent 40%),
      linear-gradient(135deg, var(--wood-warm) 0%, var(--wood-mid) 40%, var(--wood-dark) 100%);
  }
  .hero-shade { position: absolute; inset: 0; background: rgba(0,0,0,0.28); }
  .hero-content {
    position: relative; width: 880px; text-align: center;
    display: flex; flex-direction: column; align-items: center;
  }
  .company-name {
    font-family: "Dancing Script", cursive; font-weight: 700;
    font-size: 72px; margin-top: 120px; line-height: 1;
  }
  .tagline-block {
    width: 880px; margin-top: 32px;
    border-top: 1px solid var(--rule); border-bottom: 1px solid var(--rule);
    padding: 36px 0;
  }
  .tagline {
    font-family: "Amatic SC", cursive; font-weight: 400;
    font-size: 66px; line-height: 1; letter-spacing: 1px;
  }
  .cta-button {
    display: inline-block; margin-top: 88px;
    width: 284px; height: 42px; line-height: 42px;
    background: var(--accent); color: var(--ink);
    font-size: 17px; text-decoration: none;
  }

  .expect {
    height: 276px; background: var(--panel);
    display: grid; grid-template-columns: 1fr 1fr; gap: 80px;
    padding: 34px 110px 0;
  }
  .expect-title {
    font-family: "Amatic SC", cursive; font-weight: 700;
    font-size: 50px; line-height: 1; margin-bottom: 18px;
  }
  .expect-copy p { font-size: 14px; line-height: 1.6; color: var(--muted); margin-bottom: 12px; }
  .expect-copy .highlight { color: var(--accent); }

  .hours { border-top: 1px solid rgba(255,255,255,0.3); padding-top: 16px; }
  .hours-title { color: var(--accent); font-size: 14px; margin-bottom: 8px; }
  .hours-table { font-size: 13px; color: var(--accent); border-collapse: collapse; }
  .hours-table td { padding: 2px 60px 2px 0; }
  .dish-photo {
    margin-top: 16px; height: 150px;
    background: linear-gradient(160deg, #4e6b3a 0%, #8a4a2a 55%, #c9a77a 100%);
  }
</style>
</head>
<body>
  <header class="site-header">
    <div class="contact-line">1 800 000 0000 | info@yourbistro.example</div>
    <nav class="main-nav">
      <a href="#">Home</a>
      <a href="#">Menu</a>
      <a href="#">Locations</a>
    </nav>
  </header>

  <section class="hero">
    <div class="hero-photo" role="img" aria-label="Overhead view of a chef preparing tortillas, salsa and fresh vegetables on a wooden table"></div>
    <div class="hero-shade"></div>
    <div class="hero-content">
      <h1 class="company-name">Enter Company Name</h1>
      <div class="tagline-block">
        <p class="tagline">EXPERIENCE FINE DINING LIKE NEVER BEFORE!</p>
      </div>
      <a class="cta-button" href="#">Find a Table</a>
    </div>
  </section>

  <section class="expect">
    <div class="expect-copy">
      <h2 class="expect-title">What to expect</h2>
      <p>Here at our bistro we serve <span class="highlight">fine dining</span> in a warm room. Tell guests who you are and what you offer. Reach out to your market and share the dishes that will delight your diners.</p>
      <p>Short, <span class="highlight">simple</span> and straight to the point - this is your company's elevator pitch.</p>
    </div>
    <div class="expect-side">
      <div class="hours">
        <p class="hours-title">Experience The Finest In Dining</p>
        <table class="hours-table">
          <tr><td>Mon - Fri</td><td>9:00 am - 6:00 pm</td></tr>
          <tr><td>Sat - Sun</td><td>Closed</td></tr>
        </table>
      </div>
      <div class="dish-photo" role="img" aria-label="Plated dish with salad and fries on an outdoor table"></div>
    </div>
  </section>
</body>
</html>
```